Website for boutique digital agency helping high-tech startups accelerate growth.

We need a website design for a relatively young company based in Mauritius called 'LoomTrax'.

We are a professional services firm delivering digital infrastructure for revenue operations (RevOps)*.

Entrepreneurial startups and SMBs in the technology sector work with us to accelerate growth by delivering extraordinary customer experiences across the full customer lifecycle.

We would like a colourful design that utilises the (4) colours of our existing logo design.

The final design should communicate dynamic growth through relentless customer focus.
----------------------------------------------------------
*Revenue Operations (RevOps) is the strategic alignment of sales, marketing and customer success operations to accelerate growth by delivering extraordinary customer experiences across the full customer life cycle.
Updates

Target Market(s)

Entrepreneurial startups and SMBs (Small/Medium Businesses) in the technology sector.

Question: Why the technology sector?

Answer: Because technology entrepreneurs often have a tremendous challenge to effectively communicate to the market and to prospective customers the value and the benefits of their products & services due to the inherent complexity of technological innovation.

LoomTrax is a team of creatively-minded engineers and technologists who have worked with and understand the technologies and innovations our clients are passionate about bringing to market.

Industry/Entity Type

Professional Service

Number of Pages Required

5+ page

Font styles to use
Sans Serif

Requirements
Must have
• Minimalistic designs rich with visual meaning are highly preferred. Mobile responsive designs are also required. Must show how designs render on Desktop, Tablet and Smartphone devices.

Website pages:
1) Homepage: problem statement, target customers, value proposition & benefits
2) Services: 3-4 tiers of services packages with pricing and "how to work with us"
3) Resources: links to all kinds of relevant materials
4) Contact Us: contact form and special project quote form
5) Blog: matrix design with featured images for each post
Nice to have
• Bold, interesting, colourful, inspiring images that visually communicate:
- relentless customer focus
- extraordinary, memorable experiences
- business at the speed of innovation
Should not have
• Any meme or theme that panders to "political correctness".

```html
<!DOCTYPE html>
<html lang="en">
<head>
<meta charset="utf-8">
<title>LoomTrax — Digital Infrastructure for Revenue Operations</title>
<link href="https://fonts.googleapis.com/css2?family=Poppins:wght@400;500;600;700;800&family=Arimo:wght@400;700&display=swap" rel="stylesheet">
<style>
:root{
  --ink:#150f2e;
  --text:#6b6b73;
  --teal-dark:#0a4c4e;
  --teal:#0c8a88;
  --plum:#8b4159;
  --purple:#6a4ea3;
  --blue:#1a8dd8;
  --green:#52c947;
  --red:#ea3440;
  --grey:#8e8a94;
  --yellow:#e8c22b;
  --link:#e5183c;
  --black:#000;
  --white:#fff;
}
*{margin:0;padding:0;box-sizing:border-box}
html,body{width:1200px;height:2897px;overflow:hidden}
body{position:relative;background:var(--white);font-family:"Arimo",Arial,sans-serif;color:var(--text)}
.abs{position:absolute}
h1,h2,h3,h4,.brand{font-family:"Poppins",Arial,sans-serif}

/* header */
.site-header{left:0;top:0;width:1200px;height:75px;background:var(--white)}
.brand{font-weight:700;font-size:17px;color:#3a3a42;display:flex;align-items:center;gap:8px}
.brand-dot{width:14px;height:14px;background:var(--red);display:inline-block}
.site-header .brand{left:189px;top:25px}
.main-nav{top:30px;font-family:"Poppins",sans-serif;font-size:12px;letter-spacing:.6px;color:#222;font-weight:500}
.search{left:996px;top:31px}

/* hero */
.hero{left:0;top:75px;width:1200px;height:487px;background:linear-gradient(135deg,var(--teal-dark) 0%,var(--teal) 70%,#109795 100%);overflow:hidden}
.hero h1{left:174px;top:130px;color:var(--white);font-size:39px;font-weight:700;line-height:55px}
.slider-arrow{width:35px;height:63px;background:var(--black);top:169px;display:flex;align-items:center;justify-content:center}

/* section headings */
.section-title{color:var(--ink);font-weight:800;font-size:46px;line-height:46px}
.lifecycle-label{font-family:"Poppins",sans-serif;font-size:10px;font-weight:600;letter-spacing:.4px;color:#555;display:flex;align-items:center;gap:6px}
.lifecycle-label.lg{font-size:12px}

/* problem diagram */
.stage{width:112px;height:152px;display:flex;flex-direction:column}
.stage .top{height:122px;display:flex;align-items:center;justify-content:center;text-align:center;color:var(--white);font-family:"Poppins",sans-serif;font-weight:500;font-size:17px;line-height:20px}
.stage .bottom{height:30px;background:var(--grey);color:var(--white);font-size:11px;display:flex;align-items:center;justify-content:center}
.mini-arrow{top:779px}

.body-copy{font-size:14px;line-height:22.5px}

/* feature columns */
.feature{width:270px}
.feature h4{font-size:14.5px;font-weight:700;color:var(--ink);font-family:"Arimo",sans-serif;margin:0 0 10px;letter-spacing:-.1px}
.feature p{font-size:11.5px;line-height:18px}
.feature .learn{display:block;margin-top:10px;font-family:"Poppins",sans-serif;font-size:10.5px;color:var(--link);font-weight:500}
.icon{width:48px;height:48px}

/* target */
.target{left:0;top:1218px;width:1200px;height:434px;background:linear-gradient(120deg,#7e3650 0%,var(--plum) 50%,#93506a 100%)}
.target-photo{left:172px;top:53px;width:316px;height:337px;background:linear-gradient(150deg,#6b5a4a 0%,#3a4a6a 45%,#c9b7a8 100%)}
.target p{left:562px;top:183px;width:420px;color:var(--white);font-size:13.5px;line-height:22.5px}

/* value diagram */
.vp-block{display:flex;align-items:center;justify-content:center;color:var(--white);font-family:"Poppins",sans-serif;font-weight:500}

/* benefits */
.benefits{left:0;top:2269px;width:1200px;height:494px;background:linear-gradient(180deg,#e9c32c 0%,#e5be27 80%,#ddb624 100%);overflow:hidden}
.plant{right:0;top:0;width:200px;height:494px;background:radial-gradient(ellipse at 60% 40%,rgba(190,160,30,.55),rgba(232,194,43,0) 70%)}
.benefits h2{left:0;top:80px;width:1200px;text-align:center;color:var(--white);font-size:46px;font-weight:700}
.card{top:188px;height:136px;background:var(--white);border:1px solid #d8d0b0;text-align:center;padding:30px 10px 0}
.card h3{font-size:15px;font-weight:600;color:var(--ink);margin-bottom:10px;letter-spacing:.2px;white-space:nowrap}
.card p{font-size:12px;line-height:19px;color:#8a8a8a;padding:0 6px}
.car-btn{top:364px;width:40px;height:40px;background:var(--black);display:flex;align-items:center;justify-content:center}

/* footer */
.site-footer{left:0;top:2763px;width:1200px;height:134px;background:var(--black)}
.site-footer .brand{left:184px;top:46px;color:var(--white);font-size:18px}
.footer-nav{right:173px;top:42px;display:flex;gap:21px;color:var(--white);font-size:13px;font-family:"Poppins",sans-serif}
.copyright{right:173px;top:78px;color:#ccc;font-size:11px}
</style>
</head>
<body>

<header class="abs site-header">
  <div class="abs brand"><span class="brand-dot"></span>loomtrax.io</div>
  <nav>
    <span class="abs main-nav" style="left:539px">HOME</span>
    <span class="abs main-nav" style="left:603px">SERVICES</span>
    <span class="abs main-nav" style="left:688px">RESOURCES</span>
    <span class="abs main-nav" style="left:788px">BLOG</span>
    <span class="abs main-nav" style="left:849px">CONTACT US</span>
  </nav>
  <svg class="abs search" width="12" height="12" viewBox="0 0 12 12"><circle cx="5" cy="5" r="3.8" fill="none" stroke="#666" stroke-width="1.5"/><line x1="8" y1="8" x2="11" y2="11" stroke="#666" stroke-width="1.5"/></svg>
</header>

<section class="abs hero">
  <svg class="abs" style="left:690px;top:0" width="510" height="487" viewBox="0 0 510 487" role="img" aria-label="Photo of a team gathered around a laptop in a bright office">
    <defs><linearGradient id="heroPhoto" x1="0" y1="0" x2="1" y2="1"><stop offset="0" stop-color="#b58a5c"/><stop offset=".45" stop-color="#c9a58a"/><stop offset="1" stop-color="#3d3a3c"/></linearGradient></defs>
    <path d="M70 0 H510 V487 H380 C170 480 -10 330 10 190 C18 110 40 50 70 0 Z" fill="url(#heroPhoto)"/>
  </svg>
  <h1 class="abs">We delivering<br>digital infrastructure for<br>Revenue Operations</h1>
  <div class="abs slider-arrow" style="left:0"><svg width="8" height="10" viewBox="0 0 8 10"><path d="M6 1 L2 5 L6 9" stroke="#fff" stroke-width="1.5" fill="none"/></svg></div>
  <div class="abs slider-arrow" style="left:1170px;width:30px"><svg width="8" height="10" viewBox="0 0 8 10"><path d="M2 1 L6 5 L2 9" stroke="#fff" stroke-width="1.5" fill="none"/></svg></div>
</section>

<section class="problem">
  <div class="abs lifecycle-label" style="left:174px;top:695px">CUSTOMER LIFECYCLE <svg width="30" height="6" viewBox="0 0 30 6"><path d="M0 3H28M25 1L28 3L25 5" stroke="#555" fill="none"/></svg></div>
  <div class="abs stage" style="left:173px;top:716px"><div class="top" style="background:var(--purple)">Marketing</div><div class="bottom">Marketing Ops</div></div>
  <div class="abs stage" style="left:295px;top:716px"><div class="top" style="background:var(--blue)">Sales</div><div class="bottom">Sales Ops</div></div>
  <div class="abs stage" style="left:415px;top:716px"><div class="top" style="background:var(--green)">Customer<br>Success</div><div class="bottom">Customer Ops</div></div>
  <svg class="abs mini-arrow" style="left:276px" width="30" height="8" viewBox="0 0 30 8"><path d="M1 6 Q14 0 28 4M25 2L28 4L25 6" stroke="#fff" fill="none"/></svg>
  <svg class="abs mini-arrow" style="left:396px" width="30" height="8" viewBox="0 0 30 8"><path d="M1 6 Q14 0 28 4M25 2L28 4L25 6" stroke="#fff" fill="none"/></svg>

  <h2 class="abs section-title" style="left:561px;top:682px">The<br>Problem</h2>
  <p class="abs body-copy" style="left:561px;top:796px;width:470px">Most companies have legacy org structures based on how businesses were run twenty years ago. New functions have been added into this structure over time, creating leadership roles that are overly broad.</p>
  <p class="abs body-copy" style="left:561px;top:886px;width:470px">RevOps consolidates operations into one team to simplify everything.</p>

  <div class="abs feature" style="left:172px;top:966px">
    <svg class="icon" viewBox="0 0 48 48"><circle cx="22" cy="20" r="9" fill="none" stroke="var(--link)" stroke-width="2"/><circle cx="22" cy="20" r="3" fill="none" stroke="#f08a1c" stroke-width="2"/><rect x="2" y="2" width="10" height="10" fill="none" stroke="var(--link)" stroke-width="1.6"/><rect x="33" y="2" width="10" height="10" fill="none" stroke="var(--link)" stroke-width="1.6"/><path d="M4 46V36h10v10M30 46V36h10v10" fill="none" stroke="var(--link)" stroke-width="1.6"/></svg>
    <h4 style="margin-top:14px">MANAGEMENT SKILLS GAP</h4>
    <p>Lorem ipsum dolor sit amet, te veri suscipit expetendis nec, eirmod torquatos per eu. Eu nobis qualisque vim. Te sed eruditi nominavi, cu doming noster platonem mei, facilisi conse quntur eos id.</p>
    <span class="learn">LEARN MORE</span>
  </div>
  <div class="abs feature" style="left:466px;top:962px">
    <svg class="icon" viewBox="0 0 48 48"><circle cx="24" cy="6" r="4" fill="none" stroke="var(--green)" stroke-width="2"/><circle cx="10" cy="22" r="4" fill="none" stroke="var(--green)" stroke-width="2"/><circle cx="38" cy="22" r="4" fill="none" stroke="var(--green)" stroke-width="2"/><circle cx="24" cy="36" r="4" fill="none" stroke="#f08a1c" stroke-width="2"/><path d="M24 10V18M10 26V30M38 26V30M16 46Q24 38 32 46M4 34Q10 28 16 34M32 34Q38 28 44 34" fill="none" stroke="var(--green)" stroke-width="2"/></svg>
    <h4 style="margin-top:18px">MULTIPLE EVERYTHING</h4>
    <p>Lorem ipsum dolor sit amet, te veri suscipit expetendis nec, eirmod torquatos per eu. Eu nobis qualisque vim. Te sed eruditi nominavi, cu doming noster platonem mei, facilisi conse quntur eos id.</p>
    <span class="learn">LEARN MORE</span>
  </div>
  <div class="abs feature" style="left:758px;top:962px">
    <svg class="icon" viewBox="0 0 48 48"><rect x="12" y="1" width="24" height="22" fill="none" stroke="var(--teal)" stroke-width="2"/><path d="M16 7h16M16 12h16M16 17h12" stroke="var(--teal)" stroke-width="1.6"/><path d="M2 46H46M6 46V30h6v16M16 46V26h6v16M26 46V32h6v14M36 46V36h6v10" fill="none" stroke="#f08a1c" stroke-width="2"/></svg>
    <h4 style="margin-top:18px">FUZZY REPORTING RELATIONSHIPS</h4>
    <p>Lorem ipsum dolor sit amet, te veri suscipit expetendis nec, eirmod torquatos per eu. Eu nobis qualisque vim. Te sed eruditi nominavi, cu doming noster platonem mei, facilisi conse quntur eos id.</p>
    <span class="learn">LEARN MORE</span>
  </div>
</section>

<section class="abs target">
  <div class="abs target-photo" role="img" aria-label="Photo of two colleagues working together on a laptop"></div>
  <h2 class="abs section-title" style="left:561px;top:68px;color:var(--white)">Target<br>Customer</h2>
  <p class="abs">We firmly believes that the end user should always be the center of attention. While developing and implementing any process, the team must be laser-focused on making the end user’s job easier and faster. So our team constantly engages AEs to discover pain points and inefficient workflows that inhibit timely response to customers. The team also relentlessly looks for ways to push information to help AEs increase sales, such as algorithm-generated recommendations on sales automation apps and related products.</p>
</section>

<section class="value">
  <h2 class="abs section-title" style="left:172px;top:1716px">Value<br>Proposition</h2>
  <p class="abs body-copy" style="left:172px;top:1838px;width:395px">Apart from acquisition, the paradigm-shift in how revenue flows adds three more revenue drivers&nbsp; to maximize the revenue potential would be to achieve sustenance, and prepare for scale with consistent and delightful customer experience.</p>

  <div class="abs lifecycle-label lg" style="left:611px;top:1737px">CUSTOMER LIFECYCLE <svg width="34" height="6" viewBox="0 0 34 6"><path d="M0 3H32M29 1L32 3L29 5" stroke="#555" fill="none"/></svg></div>
  <div class="abs vp-block" style="left:611px;top:1764px;width:209px;height:77px;background:var(--blue);font-size:19px">Sales</div>
  <div class="abs vp-block" style="left:820px;top:1764px;width:207px;height:77px;background:var(--green);font-size:19px">Customer Success</div>
  <div class="abs vp-block" style="left:611px;top:1841px;width:416px;height:65px;background:var(--purple);font-size:19px">Marketing</div>
  <div class="abs vp-block" style="left:611px;top:1906px;width:416px;height:36px;background:var(--red);font-size:12px">Revenue Operations</div>

  <div class="abs feature" style="left:172px;top:2003px">
    <svg class="icon" viewBox="0 0 48 48"><circle cx="18" cy="30" r="17" fill="none" stroke="var(--link)" stroke-width="2"/><path d="M18 13V4M18 8Q10 2 6 6Q12 12 18 8M18 8Q26 2 30 6Q24 12 18 8" fill="none" stroke="var(--green)" stroke-width="2"/><path d="M6 22Q14 26 10 34M26 40Q24 32 32 30" fill="none" stroke="var(--link)" stroke-width="1.6"/></svg>
    <h4 style="margin-top:21px">SUSTENANCE</h4>
    <p>Lorem ipsum dolor sit amet, te veri suscipit expetendis nec, eirmod torquatos per eu. Eu nobis qualisque vim. Te sed eruditi nominavi, cu doming noster platonem mei, facilisi conse quntur eos id.</p>
    <span class="learn">LEARN MORE</span>
  </div>
  <div class="abs feature" style="left:464px;top:2008px">
    <svg class="icon" viewBox="0 0 48 48"><path d="M2 46H46M6 46V34h6v12M16 46V28h6v18M26 46V32h6v14M36 46V18h6v28" fill="none" stroke="#f08a1c" stroke-width="2"/><path d="M4 26L16 14L26 22L44 4M36 4H44V12" fill="none" stroke="var(--link)" stroke-width="2"/></svg>
    <h4 style="margin-top:16px">GROWTH STRATEGIES</h4>
    <p>Lorem ipsum dolor sit amet, te veri suscipit expetendis nec, eirmod torquatos per eu. Eu nobis qualisque vim. Te sed eruditi nominavi, cu doming noster platonem mei, facilisi conse quntur eos id.</p>
    <span class="learn">LEARN MORE</span>
  </div>
  <div class="abs feature" style="left:757px;top:2008px">
    <svg class="icon" viewBox="0 0 48 48"><rect x="16" y="12" width="16" height="14" rx="3" fill="none" stroke="var(--teal)" stroke-width="2"/><path d="M10 46V36Q10 30 18 30H30Q38 30 38 36V46M24 30V46" fill="none" stroke="var(--teal)" stroke-width="2"/><path d="M24 1L25.5 5H29L26 7.5L27 11L24 9L21 11L22 7.5L19 5H22.5Z M6 8L7 10.5H9.5L7.5 12L8 15L6 13.5L4 15L4.5 12L2.5 10.5H5Z M42 8L43 10.5H45.5L43.5 12L44 15L42 13.5L40 15L40.5 12L38.5 10.5H41Z" fill="none" stroke="var(--link)" stroke-width="1.3"/></svg>
    <h4 style="margin-top:16px">CUSTOMER EXPERIENCE</h4>
    <p>Lorem ipsum dolor sit amet, te veri suscipit expetendis nec, eirmod torquatos per eu. Eu nobis qualisque vim. Te sed eruditi nominavi, cu doming noster platonem mei, facilisi conse quntur eos id.</p>
    <span class="learn">LEARN MORE</span>
  </div>
</section>

<section class="abs benefits">
  <div class="abs plant" role="img" aria-label="Potted palm plant in a yellow pot"></div>
  <h2 class="abs">Benefits</h2>
  <div class="abs card" style="left:173px;width:266px"><h3>Marketing Intelligence</h3><p>Attribution to campaigns - understand and double down on the ones that create a delta.</p></div>
  <div class="abs card" style="left:466px;width:266px"><h3>Simplified Sales Workflows</h3><p>Create sales documents (and gather sign-offs) including service contracts or SLAs, master service agreements.</p></div>
  <div class="abs card" style="left:758px;width:269px"><h3>Pricing Management</h3><p>Create price books by accommodating different pricing plans, charge types and discounts.</p></div>
  <div class="abs car-btn" style="left:557px"><svg width="8" height="10" viewBox="0 0 8 10"><path d="M6 1 L2 5 L6 9" stroke="#fff" stroke-width="1.5" fill="none"/></svg></div>
  <div class="abs car-btn" style="left:602px"><svg width="8" height="10" viewBox="0 0 8 10"><path d="M2 1 L6 5 L2 9" stroke="#fff" stroke-width="1.5" fill="none"/></svg></div>
</section>

<footer class="abs site-footer">
  <div class="abs brand"><span class="brand-dot"></span>loomtrax.io</div>
  <nav class="abs footer-nav"><span>Home</span><span>Services</span><span>Resources</span><span>Blog</span><span>Contact Us</span></nav>
  <p class="abs copyright">©Copyright information here</p>
</footer>

</body>
</html>
```